Ridgeline Builders Guild Business card

We are looking for a new business card design with photo included.
Our business is a nonprofit construction contractor membership organization. We offer business education, assist with business setup and licensing, provide safety training, and provide a member directory.
URL: www.ridgelinebuildersguild.org
Color code:
CMYK: 0 cyan, 42 magenta, 100 yellow, 0 black for Print.
Hexidecimal: #FF9900
RGB: R 255; G 153; B 0

```html
<!DOCTYPE html>
<html lang="en">
<head>
<meta charset="utf-8">
<title>Ridgeline Builders Guild — Business Card</title>
<link rel="stylesheet" href="https://fonts.googleapis.com/css2?family=Jost:wght@300;400;700;800&display=swap">
<style>
  :root {
    --brand-orange: #f7941d;
    --ink: #353435;
    --ink-soft: #3c3b3c;
    --paper: #ffffff;
    --backdrop: #8a8a8a;
    --back-text: #7a797a;
  }
  * { margin: 0; padding: 0; box-sizing: border-box; }
  html, body { width: 1200px; height: 1200px; overflow: hidden; }
  body {
    background: var(--backdrop);
    font-family: "Jost", sans-serif;
    position: relative;
  }
  .card {
    position: absolute;
    left: 262px;
    width: 686px;
    height: 392px;
    overflow: hidden;
  }
  .card-front { top: 165px; background: var(--paper); }
  .card-back { top: 653px; background: var(--ink); }

  .org-name {
    position: absolute;
    left: 42px;
    top: 46px;
    font-weight: 800;
    font-size: 34px;
    line-height: 32px;
    letter-spacing: -0.5px;
    text-transform: uppercase;
    color: var(--ink);
  }
  .person-name {
    position: absolute;
    left: 42px;
    top: 151px;
    font-weight: 700;
    font-size: 24px;
    color: var(--ink);
    letter-spacing: 0.3px;
  }
  .person-title {
    position: absolute;
    left: 42px;
    top: 180px;
    font-weight: 300;
    font-size: 16px;
    color: var(--brand-orange);
  }
  .address {
    position: absolute;
    left: 42px;
    top: 207px;
    font-weight: 400;
    font-size: 16px;
    line-height: 19.5px;
    color: var(--ink-soft);
    font-style: normal;
  }
  .contacts {
    position: absolute;
    left: 42px;
    top: 278px;
    list-style: none;
    font-size: 16px;
    line-height: 20px;
    color: var(--ink-soft);
  }
  .contacts li { display: flex; align-items: center; gap: 9px; height: 20px; }
  .contacts svg { width: 13px; height: 13px; fill: var(--brand-orange); flex: none; }

  .portrait {
    position: absolute;
    left: 372px;
    top: 36px;
    width: 314px;
    height: 338px;
    background: linear-gradient(180deg, #3a393a 0%, var(--ink) 100%);
    border-radius: 150px 150px 0 0;
  }
  .band-orange {
    position: absolute; left: 0; top: 377px; width: 340px; height: 15px;
    background: var(--brand-orange);
  }
  .band-dark {
    position: absolute; left: 342px; top: 377px; width: 344px; height: 15px;
    background: var(--ink);
  }

  .back-name {
    position: absolute;
    left: 0; right: 0;
    top: 138px;
    text-align: center;
    font-weight: 800;
    font-size: 52px;
    line-height: 50px;
    letter-spacing: -1px;
    text-transform: uppercase;
    color: var(--back-text);
  }
</style>
</head>
<body>
  <section class="card card-front">
    <h1 class="org-name">Ridgeline<br>Builders Guild</h1>
    <h2 class="person-name">DANIEL HARGROVE</h2>
    <p class="person-title">PRESIDENT</p>
    <address class="address">4820 Alder Creek Rd.,<br>Suite #210<br>Portland, OR 97201</address>
    <ul class="contacts">
      <li><svg viewBox="0 0 16 16"><path d="M3.5 1l2.5 3-1.5 2c1 2 3 4 5 5l2-1.5 3 2.5-1.5 2.5C7.5 16 0 8.5 1 2.5z"/></svg>(555) 014-2738</li>
      <li><svg viewBox="0 0 16 16"><path d="M4 0h8a1 1 0 0 1 1 1v14a1 1 0 0 1-1 1H4a1 1 0 0 1-1-1V1a1 1 0 0 1 1-1zm1 2v10h6V2zm3 11a1 1 0 1 0 0 2 1 1 0 0 0 0-2z"/></svg>555.014.9061</li>
      <li><svg viewBox="0 0 16 16"><path d="M1 4h14v9H1zm1 1l6 4 6-4z"/></svg>support@ridgelinebg.org</li>
      <li><svg viewBox="0 0 16 16"><path d="M8 1a7 7 0 1 0 0 14A7 7 0 0 0 8 1zm0 2a5 5 0 0 1 4.6 3H10l-1 2 1 2-1 3a5 5 0 0 1-5-8l2 1 1 2 1-2-1-2z"/></svg>www.ridgelinebuildersguild.org</li>
    </ul>
    <div class="portrait" role="img" aria-label="Portrait photo of the card holder in a dark suit"></div>
    <div class="band-orange"></div>
    <div class="band-dark"></div>
  </section>

  <section class="card card-back">
    <p class="back-name">Ridgeline<br>Builders Guild</p>
  </section>
</body>
</html>
```